Tomas's Business Cards

My husband is a self employed Cabinet Maker... who contracts to Building companies and clients directly.
He installs kitchesn, designs and also completes renovations and building work.

I would like a small, FUNKY, simple but eye catching design.

It needs to incorporate the following.
Custom Cabinets / Installations / Renovations / Design

Commercial and Residential

He does not have a Website or Chatterly,
contact number is 0438 207 619 and email is tomasvelkin@quillmail.example

I would like a Grey/Silver on black, or blue covering.. I am open to colour designs?

Thank you. :-)

Target Market(s)

Building Companies
Clients
Other Trades people onsite,. to give out at job sites

Industry/Entity Type

Business

Contact Information for Business Card

Phone: 0438 207 619
Email: tomasvelkin@quillmail.example

Font styles to use
Sans Serif

Colors
0592cd
747474
474747
1b1b1b
85cae6

Requirements
Must have
• Funky, simple, eye catching design
• Would like use of Silver/Grey - and a colour that would complement this.
• Am open to ideas :-)
Nice to have
• We do not have a logo or picture, will leave this up to you if you think an image would be beneficial???
• Thank you.

```html
<!DOCTYPE html>
<html lang="en">
<head>
<meta charset="UTF-8">
<title>Custom Cabinets – Business Card</title>
<link href="https://fonts.googleapis.com/css2?family=Source+Sans+3:wght@400;600&display=swap" rel="stylesheet">
<style>
  :root {
    --backdrop: #2a2a2a;
    --card-white: #ffffff;
    --ink: #1b1b1b;
    --ink-soft: #474747;
    --accent-blue: #0592cd;
    --accent-sky: #85cae6;
    --silver: #747474;
    --wood-light: #e2b48e;
    --wood-mid: #c98f62;
    --wood-deep: #8a5434;
    --shadow: rgba(0, 0, 0, 0.55);
  }
  html, body {
    margin: 0;
    padding: 0;
    width: 1200px;
    height: 900px;
    overflow: hidden;
    background: var(--backdrop);
  }
  .canvas {
    position: relative;
    width: 1200px;
    height: 900px;
    display: flex;
    align-items: center;
    justify-content: center;
  }
  .business-card {
    position: relative;
    width: 1000px;
    height: 600px;
    display: flex;
    background: var(--card-white);
    box-shadow: 0 20px 50px var(--shadow);
    overflow: hidden;
  }
  .card-info {
    flex: 0 0 580px;
    padding: 155px 0 0 90px;
    box-sizing: border-box;
    font-family: "Source Sans 3", "Myriad Pro", sans-serif;
  }
  .company-name {
    margin: 0 0 56px;
    font-weight: 600;
    font-size: 60px;
    line-height: 1;
    color: var(--ink);
  }
  .service-list {
    list-style: none;
    margin: 0;
    padding: 0 0 0 40px;
    font-size: 25px;
    font-weight: 400;
    line-height: 40px;
    color: var(--ink-soft);
  }
  .card-divider {
    flex: 0 0 22px;
    background: var(--accent-blue);
  }
  .card-photo {
    flex: 1;
    background: linear-gradient(160deg, var(--wood-light) 0%, var(--wood-mid) 50%, var(--wood-deep) 100%);
  }
</style>
</head>
<body>
  <main class="canvas">
    <article class="business-card">
      <section class="card-info">
        <h1 class="company-name">Custom Cabinets</h1>
        <ul class="service-list">
          <li>Installations</li>
          <li>Renovations</li>
          <li>Design Commercial and Residential</li>
          <li>Phone: 0438 207 619</li>
          <li>Email: tomasvelkin@quillmail.example</li>
        </ul>
      </section>
      <div class="card-divider"></div>
      <div class="card-photo" role="img" aria-label="Photo of light timber kitchen cabinets with benchtop and open shelving"></div>
    </article>
  </main>
</body>
</html>
```